Figure for a research paper

I am working on designing a figure for a research paper that illustrates the effect of KORA Pathway assessment on student outcomes over time by impacting teacher bias and teacher perception of student growth. I built the attached figure via powerpoint. It includes the very basic elements but it does not look great and I am not sure that it is clearly depicting what I am hoping to illustrate. I would like for you to build an illustration of this idea that i can include in the paper.

```html
<!DOCTYPE html>
<html lang="en">
<head>
<meta charset="utf-8">
<title>Effect of KORA Pathway Assessment on SEL Program Effectiveness</title>
<link rel="stylesheet" href="https://fonts.googleapis.com/css2?family=Source+Sans+3:wght@400&display=swap">
<style>
  :root {
    --bg: #18355f;
    --axis: #8fd6cc;
    --perceived: #f7c97a;
    --actual: #e0323a;
    --label: #ffffff;
    --fig-label: #c9d2de;
    --bar-fill: #2d4874;
    --bar-stroke: #5d739b;
    --arrow: #6a82aa;
    --area-top: #1f3c68;
    --area-bottom: #324f7c;
  }
  html, body {
    margin: 0;
    padding: 0;
    width: 1200px;
    height: 1200px;
    overflow: hidden;
    background: var(--bg);
  }
  .figure-sheet {
    display: block;
    width: 1200px;
    height: 1200px;
  }
  .axis { stroke: var(--axis); stroke-width: 4.5; stroke-linecap: round; fill: none; }
  .line-perceived { stroke: var(--perceived); stroke-width: 1.2; fill: none; }
  .line-actual { stroke: var(--actual); stroke-width: 1.2; fill: none; }
  .dot-perceived { fill: var(--perceived); }
  .dot-actual { fill: var(--actual); }
  .factor-bar { fill: var(--bar-fill); stroke: var(--bar-stroke); stroke-width: 1; }
  .label {
    font-family: "Source Sans 3", sans-serif;
    font-size: 13.7px;
    fill: var(--label);
  }
  .label-center { text-anchor: middle; }
  .fig-number {
    font-family: "Source Sans 3", sans-serif;
    font-size: 20px;
    fill: var(--fig-label);
    letter-spacing: 0.3px;
  }
</style>
</head>
<body>
<svg class="figure-sheet" viewBox="0 0 1200 1200" xmlns="http://www.w3.org/2000/svg">
  <defs>
    <linearGradient id="area-fill" x1="0" y1="0" x2="0" y2="1">
      <stop offset="0" stop-color="var(--area-top)"/>
      <stop offset="1" stop-color="var(--area-bottom)"/>
    </linearGradient>
    <linearGradient id="arrow-down" x1="0" y1="0" x2="0" y2="1">
      <stop offset="0" stop-color="var(--arrow)" stop-opacity="0"/>
      <stop offset="1" stop-color="var(--arrow)" stop-opacity="1"/>
    </linearGradient>
    <linearGradient id="arrow-up" x1="0" y1="1" x2="0" y2="0">
      <stop offset="0" stop-color="var(--arrow)" stop-opacity="0"/>
      <stop offset="1" stop-color="var(--arrow)" stop-opacity="1"/>
    </linearGradient>
  </defs>

  <!-- Figure 1: perceived effectiveness without assessment -->
  <g class="chart chart-baseline">
    <polygon class="effect-area" fill="url(#area-fill)" points="373,374 838,302 838,447 373,447"/>
    <line class="axis axis-y" x1="371" y1="130" x2="371" y2="463"/>
    <line class="axis axis-x" x1="352" y1="447" x2="944" y2="447"/>
    <line class="line-perceived" x1="373" y1="374" x2="842" y2="302"/>
    <circle class="dot-perceived" cx="373" cy="374" r="3.5"/>
    <circle class="dot-perceived" cx="842" cy="302" r="3.5"/>

    <text class="label axis-title">
      <tspan x="261" y="261">Effectiveness of</tspan>
      <tspan x="261" y="278">SEL Program on</tspan>
      <tspan x="261" y="294">the Student</tspan>
    </text>
    <text class="label label-center" x="614" y="473">Time</text>

    <text class="label label-center" x="488" y="289">Teacher Bias</text>
    <rect class="factor-bar" x="433.5" y="302.5" width="116" height="10"/>
    <path fill="url(#arrow-down)" d="M446.5,314 L455.5,314 L455.5,339 L463.5,339 L451,355 L438.5,339 L446.5,339Z"/>
    <path fill="url(#arrow-down)" d="M516.5,314 L525.5,314 L525.5,329 L533.5,329 L521,345 L508.5,329 L516.5,329Z"/>

    <text class="label">
      <tspan x="707" y="217">Teacher’s inaccurate</tspan>
      <tspan x="707" y="234">perception of student</tspan>
      <tspan x="707" y="250">growth (or learning)</tspan>
    </text>
    <rect class="factor-bar" x="697.5" y="261.5" width="151" height="10"/>
    <path fill="url(#arrow-down)" d="M723.5,273 L732.5,273 L732.5,298 L740.5,298 L728,314 L715.5,298 L723.5,298Z"/>
    <path fill="url(#arrow-down)" d="M794.5,273 L803.5,273 L803.5,287 L811.5,287 L799,303 L786.5,287 L794.5,287Z"/>

    <text class="fig-number" x="894" y="498">FIg. 1</text>
  </g>

  <!-- Figure 2: effectiveness with KORA Pathway assessment -->
  <g class="chart chart-assessment">
    <polygon class="effect-area" fill="url(#area-fill)" points="373,989 838,774 838,1063 373,1063"/>
    <line class="axis axis-y" x1="371" y1="666" x2="371" y2="1079"/>
    <line class="axis axis-x" x1="352" y1="1063" x2="944" y2="1063"/>
    <line class="line-actual" x1="373" y1="989" x2="838" y2="774"/>
    <line class="line-perceived" x1="373" y1="989" x2="842" y2="917"/>
    <circle class="dot-perceived" cx="373" cy="989" r="3.5"/>
    <circle class="dot-perceived" cx="842" cy="917" r="3.5"/>
    <circle class="dot-actual" cx="838" cy="774" r="3.5"/>

    <text class="label axis-title">
      <tspan x="261" y="825">Effectiveness of</tspan>
      <tspan x="261" y="842">SEL Program on</tspan>
      <tspan x="261" y="858">the Student</tspan>
    </text>
    <text class="label label-center" x="614" y="1089">Time</text>

    <text class="label label-center" x="488" y="858">Teacher Bias</text>
    <rect class="factor-bar" x="433.5" y="872.5" width="116" height="10"/>
    <path fill="url(#arrow-down)" d="M446.5,884 L455.5,884 L455.5,933 L463.5,933 L451,949 L438.5,933 L446.5,933Z"/>
    <path fill="url(#arrow-down)" d="M516.5,884 L525.5,884 L525.5,899 L533.5,899 L521,915 L508.5,899 L516.5,899Z"/>

    <text class="label">
      <tspan x="707" y="697">Teacher’s inaccurate</tspan>
      <tspan x="707" y="714">perception of student</tspan>
      <tspan x="707" y="730">growth (or learning)</tspan>
    </text>
    <rect class="factor-bar" x="697.5" y="740.5" width="151" height="10"/>
    <path fill="url(#arrow-down)" d="M723.5,753 L732.5,753 L732.5,799 L740.5,799 L728,815 L715.5,799 L723.5,799Z"/>
    <path fill="url(#arrow-down)" d="M794.5,753 L803.5,753 L803.5,768 L811.5,768 L799,784 L786.5,768 L794.5,768Z"/>

    <path fill="url(#arrow-up)" d="M743.5,856 L752.5,856 L752.5,842 L760.5,842 L748,826 L735.5,842 L743.5,842Z"/>
    <path fill="url(#arrow-up)" d="M813.5,856 L822.5,856 L822.5,807 L830.5,807 L818,791 L805.5,807 L813.5,807Z"/>
    <rect class="factor-bar" x="719.5" y="858.5" width="116" height="10"/>
    <text class="label label-center">
      <tspan x="777" y="888">KORA Pathway</tspan>
      <tspan x="777" y="905">Assessment</tspan>
    </text>

    <text class="fig-number" x="894" y="1125">FIg. 2</text>
  </g>
</svg>
</body>
</html>
```